Evergrove Yard Service and Beyond LLC

• Mowing
• Weed eating
•Edging
• hedge trimming
• landscaping
•mulching
•yard clean up
• pressure washing

Target Market(s)

Everyone

Contact Information for Business Card

Licensed and insured

Font styles to use
Serif

Colors
59FF00
82FF00
B8FF75
E3FFCB
F4FFEA
F0912C
F2A743
F7CA91
FBE8D2
FDF5EE
EE7325
F08F49
F5BC92
FAE3D3
FDF4ED
EB3D1F
EC4F4E
F09395
F8D3D4
FCEDEE
E54698
E96AAD
F1A4CE
F9D9EA
FCEFF6

```html
<!DOCTYPE html>
<html lang="en">
<head>
<meta charset="utf-8">
<title>Evergrove Yard Service and Beyond LLC — Business Card</title>
<link href="https://fonts.googleapis.com/css2?family=Montserrat:wght@400;500;700;800&family=Oswald:wght@500&display=swap" rel="stylesheet">
<style>
  :root {
    --bg: #3a3a3a;
    --forest: #0c4d33;
    --leaf: #7cc242;
    --ink: #1f1f1f;
    --white: #ffffff;
    --radius: 34px;
  }
  * { box-sizing: border-box; margin: 0; padding: 0; }
  html, body { width: 1200px; height: 1200px; overflow: hidden; }
  body {
    background: var(--bg);
    font-family: "Montserrat", sans-serif;
    position: relative;
  }
  .card {
    position: absolute;
    left: 150px;
    width: 900px;
    height: 514px;
    border-radius: var(--radius);
    overflow: hidden;
  }
  .card-front { top: 58px; background: var(--white); }
  .card-back { top: 628px; background: var(--forest); }

  .front-wave { position: absolute; inset: 0; width: 100%; height: 100%; }

  .contact-block {
    position: absolute;
    left: 70px;
    top: 170px;
    z-index: 1;
  }
  .person-name {
    font-weight: 700;
    font-size: 44px;
    color: var(--leaf);
    letter-spacing: 0.5px;
    line-height: 1;
  }
  .person-role {
    font-weight: 500;
    font-size: 20px;
    color: var(--ink);
    letter-spacing: 1px;
    margin-top: 6px;
  }
  .contact-list { list-style: none; margin-top: 14px; }
  .contact-item {
    display: flex;
    align-items: center;
    gap: 14px;
    font-size: 22px;
    color: var(--ink);
    height: 36px;
  }
  .contact-icon { width: 24px; height: 24px; flex: none; }

  .brand-front {
    position: absolute;
    right: 60px;
    top: 70px;
    width: 360px;
    text-align: center;
    font-weight: 800;
    font-size: 30px;
    line-height: 1.15;
    color: var(--forest);
    text-transform: uppercase;
    letter-spacing: 1px;
    z-index: 1;
  }

  .brand-back {
    position: absolute;
    left: 0;
    right: 0;
    top: 110px;
    text-align: center;
    font-weight: 800;
    font-size: 46px;
    line-height: 1.15;
    color: var(--white);
    text-transform: uppercase;
    letter-spacing: 2px;
  }

  .service-grid {
    position: absolute;
    left: 70px;
    right: 60px;
    bottom: 58px;
    display: flex;
    justify-content: space-between;
  }
  .service-column { list-style: none; }
  .service-item {
    font-family: "Oswald", sans-serif;
    font-weight: 500;
    font-size: 24px;
    color: var(--white);
    text-transform: uppercase;
    line-height: 1.3;
    display: flex;
    align-items: center;
    gap: 10px;
  }
  .service-item::before {
    content: "";
    width: 8px;
    height: 8px;
    border-radius: 50%;
    background: var(--leaf);
    flex: none;
  }
</style>
</head>
<body>

  <section class="card card-front" aria-label="Card front">
    <svg class="front-wave" viewBox="0 0 900 514" preserveAspectRatio="none" aria-hidden="true">
      <path d="M0 470 C 250 410, 500 440, 650 350 C 760 285, 840 225, 900 215 L 900 514 L 0 514 Z" fill="var(--leaf)"/>
      <path d="M0 486 C 250 426, 500 456, 650 366 C 760 301, 840 241, 900 231 L 900 514 L 0 514 Z" fill="var(--white)"/>
      <path d="M0 500 C 250 440, 500 470, 650 380 C 760 315, 840 255, 900 245 L 900 514 L 0 514 Z" fill="var(--forest)"/>
    </svg>

    <div class="brand-front">Evergrove Yard Service and Beyond LLC</div>

    <div class="contact-block">
      <h1 class="person-name">FULL NAME</h1>
      <p class="person-role">POSITION</p>
      <ul class="contact-list">
        <li class="contact-item">
          <svg class="contact-icon" viewBox="0 0 24 24" aria-hidden="true"><path d="M6.6 10.8a15 15 0 0 0 6.6 6.6l2.2-2.2a1 1 0 0 1 1-.25 11.4 11.4 0 0 0 3.6.57 1 1 0 0 1 1 1V20a1 1 0 0 1-1 1A17 17 0 0 1 3 4a1 1 0 0 1 1-1h3.5a1 1 0 0 1 1 1c0 1.25.2 2.450.57 3.57a1 1 0 0 1-.25 1z" fill="var(--leaf)"/></svg>
          (000) 000 0000
        </li>
        <li class="contact-item">
          <svg class="contact-icon" viewBox="0 0 24 24" aria-hidden="true"><rect x="2" y="5" width="20" height="14" rx="1" fill="var(--leaf)"/><path d="M2.5 6 12 13l9.5-7" fill="none" stroke="var(--white)" stroke-width="1.6"/></svg>
          email@evergrove.com
        </li>
        <li class="contact-item">
          <svg class="contact-icon" viewBox="0 0 24 24" aria-hidden="true"><g fill="none" stroke="var(--leaf)" stroke-width="1.8"><circle cx="12" cy="12" r="10"/><ellipse cx="12" cy="12" rx="4.5" ry="10"/><path d="M2 12h20M4 7h16M4 17h16"/></g></svg>
          www.evergrove.com
        </li>
      </ul>
    </div>
  </section>

  <section class="card card-back" aria-label="Card back">
    <div class="brand-back">Evergrove Yard Service<br>and Beyond LLC</div>

    <div class="service-grid">
      <ul class="service-column">
        <li class="service-item">Mowing</li>
        <li class="service-item">Weed Eating</li>
      </ul>
      <ul class="service-column">
        <li class="service-item">Edging</li>
        <li class="service-item">Hedge Trimming</li>
      </ul>
      <ul class="service-column">
        <li class="service-item">Landscaping</li>
        <li class="service-item">Mulching</li>
      </ul>
      <ul class="service-column">
        <li class="service-item">Yard Clean Up</li>
        <li class="service-item">Pressure Washing</li>
      </ul>
    </div>
  </section>

</body>
</html>
```